St. Paddy’s Day Invitation

Invitation to text to people:
6th Annual St. Paddy’s Day Party
Where: The Kelterbrook’s
When: Saturday, March 25
Acoustic session by Taddeo Lindqvist from Mr. Pocketwatch
Fundraiser for Milo Ferreday ‘Open Harbor’ Fund

Target Market(s)

Adults only, all friends from our town, Moorestown, NJ

Colors
00AB8E
00BBA5
67D7C9
C6EFE9
E9F9F6
59FF00
82FF00
B8FF75
E3FFCB
F4FFEA

```html
<!DOCTYPE html>
<html lang="en">
<head>
<meta charset="utf-8">
<title>6th Annual St. Paddy’s Day Party</title>
<link rel="stylesheet" href="https://fonts.googleapis.com/css2?family=Arimo:ital,wght@0,400;0,700;1,400&family=Roboto+Condensed:wght@700&family=Pinyon+Script&display=swap">
<style>
  :root {
    --page: #ffffff;
    --poster-green: #1b5e3b;
    --headline-yellow: #f6c700;
    --detail-gold: #c9a56a;
    --label-white: #ffffff;
    --panel-white: #ffffff;
    --ink: #1d1d1b;
    --muted-grey: #8f8f8f;
    --fund-navy: #22345f;
  }
  * { margin: 0; padding: 0; box-sizing: border-box; }
  html, body { width: 1200px; height: 1000px; overflow: hidden; background: var(--page); }
  .canvas { position: relative; width: 1200px; height: 1000px; }
  .invitation {
    position: absolute; left: 290px; top: 84px; width: 626px; height: 843px;
    background: var(--poster-green);
  }
  .edition {
    position: absolute; left: 0; right: 0; top: 52px; text-align: center;
    font: 700 27px/1 "Arimo", Arial, sans-serif; letter-spacing: 3px;
    color: var(--headline-yellow);
  }
  .headline-top {
    position: absolute; left: 0; right: 0; top: 104px; text-align: center;
    font: 700 78px/1 "Roboto Condensed", "Arial Narrow", sans-serif;
    color: var(--headline-yellow);
  }
  .headline-script { position: absolute; left: 0; top: 150px; width: 626px; height: 200px; overflow: visible; }
  .headline-script text {
    font-family: "Pinyon Script", cursive; font-size: 142px;
    fill: var(--label-white); stroke: var(--ink); stroke-width: 7px;
    paint-order: stroke fill; stroke-linejoin: round;
  }
  .details { position: absolute; left: 118px; top: 386px; }
  .detail-row { display: flex; align-items: baseline; height: 34px; }
  .detail-label { width: 92px; font: 400 21px/1 "Arimo", Arial, sans-serif; color: var(--label-white); white-space: pre; }
  .detail-value { font: 700 29px/1 "Arimo", Arial, sans-serif; color: var(--detail-gold); }
  .feature-panel {
    position: absolute; left: 37px; top: 493px; width: 551px; height: 305px;
    background: var(--panel-white);
  }
  .performer-photo {
    position: absolute; left: 0; top: 0; width: 195px; height: 305px;
    background: linear-gradient(90deg, #ffffff 0%, #6b6b6b 35%, #2a2a2a 60%, #d9d9d9 100%);
  }
  .feature-text { position: absolute; left: 210px; font-family: "Arimo", Arial, sans-serif; }
  .performer { top: 36px; }
  .fundraiser { top: 197px; }
  .intro { font: italic 400 21px/1.2 "Arimo", Arial, sans-serif; color: var(--muted-grey); }
  .name { font: 700 24px/1.2 "Arimo", Arial, sans-serif; color: var(--ink); }
  .connector { color: var(--muted-grey); }
  .fund-mark {
    position: absolute; left: 383px; top: 178px; width: 160px;
    display: flex; align-items: center; gap: 6px;
    font: 700 16px/1 "Arimo", Arial, sans-serif; color: var(--fund-navy); white-space: nowrap;
  }
  .fund-mark .dot { width: 10px; height: 10px; border-radius: 50%; background: var(--fund-navy); flex: none; }
</style>
</head>
<body>
<main class="canvas">
  <section class="invitation">
    <p class="edition">6th ANNUAL</p>
    <h1>
      <span class="headline-top">St. Paddy’s</span>
      <svg class="headline-script" viewBox="0 0 626 200" aria-label="Day Party">
        <text x="313" y="150" text-anchor="middle">Day Party</text>
      </svg>
    </h1>
    <div class="details">
      <p class="detail-row"><span class="detail-label">Where :</span><span class="detail-value">The Kelterbrook’s</span></p>
      <p class="detail-row"><span class="detail-label">When  :</span><span class="detail-value">Saturday, March 25</span></p>
    </div>
    <div class="feature-panel">
      <div class="performer-photo" role="img" aria-label="Black and white photo of the performer singing into a microphone"></div>
      <div class="feature-text performer">
        <p class="intro">Acoustic session by</p>
        <p class="name">Taddeo Lindqvist</p>
        <p class="name"><span class="connector">from</span> Mr. Pocketwatch</p>
      </div>
      <div class="fund-mark"><span class="dot"></span>Open Harbor Fund</div>
      <div class="feature-text fundraiser">
        <p class="intro">Fundraiser for</p>
        <p class="name">Milo Ferreday</p>
        <p class="name">‘Open Harbor’ Fund</p>
      </div>
    </div>
  </section>
</main>
</body>
</html>
```